New Design for Brightcoilheat [Zimpla]

Hello, This is my 2nd project here. I need a new web design for www.brightcoilheat.com.au which is one of my clients, and an extremely outdated website. It only has a few links and is fairly straight forward, looking for a more professional, up-to-date looking website. Please note: The website will be made under a zimpla white-label platform, so the design MUST be consistent with this type of platform. Many more projects will be up and coming so the best designers will definitely be selected for future projects.
Thankyou

• Please refer to www.brightcoilheat.com.au to find all the content.

```html
<!DOCTYPE html>
<html lang="en">
<head>
<meta charset="utf-8">
<title>Brightcoilheat Pty Ltd</title>
<link href="https://fonts.googleapis.com/css2?family=Bebas+Neue&family=Arimo:wght@400;700&family=Open+Sans:wght@400&display=swap" rel="stylesheet">
<style>
:root{
  --bg-deep:#0a1a6b;
  --bg-mid:#1533b8;
  --nav-blue:#0b35e0;
  --nav-light:#3a66ff;
  --brand-blue:#0033ff;
  --link-blue:#0022cc;
  --title-blue:#0a3ad8;
  --ink:#222;
  --body-grey:#555;
  --rule:#8a8a8a;
  --side-row:#dcdcdc;
  --footer-dark:#151515;
}
*{margin:0;padding:0;box-sizing:border-box}
html,body{width:1200px;height:1065px;overflow:hidden}
body{
  background:linear-gradient(90deg,var(--bg-deep) 0%,var(--bg-mid) 9%,var(--bg-deep) 15%,var(--bg-deep) 85%,var(--bg-mid) 91%,var(--bg-deep) 100%);
  font-family:"Arimo",Arial,sans-serif;position:relative;
}
.page{position:absolute;left:115px;top:0;width:960px;height:1013px;background:#fff;box-shadow:0 0 8px rgba(0,0,0,.5)}
.masthead{position:absolute;left:0;top:0;width:960px;height:118px;
  background:linear-gradient(90deg,#5a5a5a,#c8c8c8 20%,#777 40%,#dcdcdc 55%,#6b6b6b 75%,#e0e0e0 90%,#555);}
.brand{position:absolute;left:29px;top:22px;display:flex;align-items:center;gap:12px}
.brand-mark{width:75px;height:75px;background:var(--brand-blue)}
.brand-name{font-family:"Arimo",Arial,sans-serif;font-weight:700;font-size:22px;color:#fff}
.mainnav{position:absolute;left:0;top:118px;width:960px;height:60px;
  background:linear-gradient(180deg,var(--nav-light),var(--nav-blue) 45%,#0828b8);
  border:1px solid #6f8cff;display:flex;align-items:center;padding-left:33px}
.mainnav a{font-family:"Open Sans",sans-serif;color:#fff;text-decoration:none;font-size:15px;text-transform:uppercase}
.mainnav .sep{width:1px;height:14px;border-left:1px dotted #6f8cff;margin:0 35px}
.sidebar{position:absolute;left:18px;top:200px;width:240px}
.side-head{height:40px;background:linear-gradient(180deg,#f2f2f2,#bdbdbd 55%,#9a9a9a);
  border:1px solid #999;position:relative;text-align:center;
  font-family:"Bebas Neue",sans-serif;font-size:24px;line-height:42px;color:#1c1c1c}
.side-head .screw{position:absolute;top:13px;width:14px;height:14px;border-radius:50%;
  background:radial-gradient(circle,#ddd,#666);border:1px solid #444}
.side-head .screw.l{left:8px}.side-head .screw.r{right:8px}
.side-list{list-style:none;background:linear-gradient(90deg,#d0d0d0,#e8e8e8)}
.side-list li{height:30px;line-height:30px;padding-left:18px;font-size:14px;color:#333;
  border-bottom:1px solid #fff;box-shadow:inset 0 -1px 0 #bbb;text-transform:uppercase;letter-spacing:.3px}
.side-list li.sub{height:27px;line-height:27px;padding-left:44px;text-transform:none;font-size:13.5px;position:relative}
.side-list li.sub::before{content:"›";position:absolute;left:28px;font-size:11px}
.office{height:294px;background:linear-gradient(180deg,#d8d8d8,#bdbdbd);border:1px solid #aaa;padding:16px 13px;font-size:13px;color:#222;line-height:17px}
.office-photo{width:208px;height:88px;background:#7e7e7e;border:2px solid #fff;margin:0 0 16px 2px}
.office p+p{margin-top:17px}
.office .lbl{display:inline-block;width:73px}
.section{position:absolute;left:286px;width:650px}
.section h2{font-family:"Bebas Neue",sans-serif;font-weight:400;font-size:21px;color:#1a1a1a;height:26px;line-height:28px;
  border-bottom:2px solid var(--rule);width:636px;position:relative}
.section h2::after{content:"";position:absolute;left:0;bottom:-2px;width:386px;height:2px;background:#333}
.entry{position:relative;margin-top:16px;padding-left:104px;min-height:94px}
.thumb{position:absolute;left:0;top:0;width:90px;height:94px;border:1px solid #bbb;padding:3px}
.thumb span{display:block;width:100%;height:100%;background:#808080}
.entry h3{font-size:12.5px;color:var(--title-blue);font-weight:700;letter-spacing:.5px;line-height:14px}
.entry p{font-size:10.8px;line-height:13px;color:var(--body-grey);width:550px}
.links{display:grid;grid-template-columns:220px 220px;margin:11px 0 0 124px;font-size:10.8px;row-gap:1px}
.links a{color:var(--link-blue);line-height:15px}
.links div{color:#333}
.more{position:absolute;right:0;font-size:10px;color:#111}
.footer{position:absolute;left:0;top:952px;width:960px;height:61px;background:linear-gradient(180deg,#333,var(--footer-dark));
  display:flex;align-items:center;padding-left:12px;font-family:"Open Sans",sans-serif;font-size:11.5px;color:#eee}
.footer .mark{width:32px;height:34px;background:#555;margin-right:19px}
</style>
</head>
<body>
<div class="page">
  <header class="masthead" role="img" aria-label="Greyscale collage of industrial insulation products and machinery">
    <div class="brand"><div class="brand-mark"></div><span class="brand-name">Brightcoilheat</span></div>
  </header>
  <nav class="mainnav">
    <a href="#">Home</a><span class="sep"></span>
    <a href="#">About Us</a><span class="sep"></span>
    <a href="#">Products</a><span class="sep"></span>
    <a href="#">Services</a><span class="sep"></span>
    <a href="#">Contact Us</a>
  </nav>

  <aside class="sidebar">
    <div class="side-head"><span class="screw l"></span>Thermal Products<span class="screw r"></span></div>
    <ul class="side-list">
      <li>Product Category</li>
      <li class="sub">Product Sub Category</li>
      <li class="sub">Product Sub Category</li>
      <li class="sub">Product Sub Category</li>
      <li>Product Category</li>
      <li>Product Category</li>
      <li>Product Category</li>
      <li>Product Category</li>
      <li>Product Category</li>
    </ul>
    <div class="side-head"><span class="screw l"></span>Our Services<span class="screw r"></span></div>
    <ul class="side-list">
      <li>Service Category</li>
      <li>Service Category</li>
    </ul>
    <div class="side-head"><span class="screw l"></span>Our Office<span class="screw r"></span></div>
    <div class="office">
      <div class="office-photo" role="img" aria-label="Photo of the office building"></div>
      <p>Brightcoilheat Pty Ltd<br>18 Harlow Court<br>Kingsford East 3190<br>Victoria Australia</p>
      <p><span class="lbl">Telephone:</span>+61 3 5550 1427<br><span class="lbl">FAX:</span>+61 3 5550 1432<br>E-mail: sales@brightcoilheat.com.au<br>Contact: Alan Brooks - Dean Porter</p>
    </div>
  </aside>

  <section class="section" style="top:205px">
    <h2>Welcome to Brightcoilheat Pty Ltd</h2>
    <div class="entry">
      <div class="thumb" role="img" aria-label="Product photo"><span></span></div>
      <h3>Integer rutrum ante eu lacus.</h3>
      <p>consec tetuer adipiscing elit. Praesent vestib ulum molest lacus aenean nonummy hendrerit mauris. Phasellus porta fusce suscipit varius mi. Cum sociis natoque penatibus et magnis.dis parturient montes, nascetur ridiculus mus. Nulla dui. Fusce feugiat malesuada odio. Morbi nunc odio, gravida at, cursus nec, luctus a, lorem.onsec tetuer adipiscing elit. Praesent vestib ulum molest lacus aenean nonummy hendrerit mauris. Phasellus porta fusce suscipit varius mi. Cum sociis natoque penatibus et magnis.dis parturient montes, nascetur ridiculus mus. Nulla dui. Fusce feugiat malesuada odio. Morbi nunc odio, gravida at, cursus nec, luctus a, lorem.</p>
      <span class="more" style="top:88px">[READ MORE]</span>
    </div>
  </section>

  <section class="section" style="top:355px">
    <h2>Our Services</h2>
    <div class="entry">
      <div class="thumb" role="img" aria-label="Service photo"><span></span></div>
      <h3>Integer rutrum ante eu lacus.</h3>
      <p>consec tetuer adipiscing elit. Praesent vestib ulum molest lacus aenean nonummy hendrerit mauris. Phasellus porta fusce suscipit varius mi. Cum sociis natoque penatibus et magnis.dis parturient montes, nascetur ridiculus mus. Nulla dui. Fusce feugiat malesuada odio. Morbi nunc odio, gravida at, cursus nec, luctus a, lorem.onsec tetuer adipiscing elit. Praesent vestib ulum molest lacus aenean nonummy hendrerit mauris. Phasellus porta fusce suscipit varius mi. Cum sociis natoque penatibus et magnis.dis parturient montes, nascetur ridiculus mus. Nulla dui. Fusce feugiat malesuada odio. Morbi nunc odio, gravida at, cursus nec, luctus a, lorem.</p>
    </div>
    <div class="links">
      <div>- <a href="#">Lorem ipsum dolorit amet tetuer</a></div><div>- <a href="#">Lorem ipsum dolorit amet tetuer</a></div>
      <div>- <a href="#">Adipiscing elit praesebutm molestie lacus</a></div><div>- <a href="#">Adipiscing elit praesebutm molestie lacus</a></div>
      <div>- <a href="#">Lorem ipsum dolorit amet tetuer</a></div><div>- <a href="#">Lorem ipsum dolorit amet tetuer</a></div>
      <div>- <a href="#">Adipiscing elit praesebutm molestie lacus</a></div><div>- <a href="#">Adipiscing elit praesebutm molestie lacus</a></div>
      <div>- <a href="#">Lorem ipsum dolorit amet tetuer</a></div><div>- <a href="#">Lorem ipsum dolorit amet tetuer</a></div>
      <div>- <a href="#">Adipiscing elit praesebutm molestie lacus</a></div><div>- <a href="#">Adipiscing elit praesebutm molestie lacus</a></div>
    </div>
    <span class="more" style="top:229px">[READ MORE]</span>
  </section>

  <section class="section" style="top:605px">
    <h2>Why Brightcoilheat Pty Ltd</h2>
    <div class="entry">
      <div class="thumb" role="img" aria-label="Workshop photo"><span></span></div>
      <h3>Integer rutrum ante eu lacus.</h3>
      <p>consec tetuer adipiscing elit. Praesent vestib ulum molest lacus aenean nonummy hendrerit mauris. Phasellus porta fusce suscipit varius mi. Cum sociis natoque penatibus et magnis.dis parturient montes, nascetur ridiculus mus. Nulla dui. Fusce feugiat malesuada odio. Morbi nunc odio, gravida at, cursus nec, luctus a, lorem.onsec tetuer adipiscing elit. Praesent vestib ulum molest lacus aenean nonummy hendrerit mauris. Phasellus porta fusce suscipit varius mi. Cum sociis natoque penatibus et magnis.dis parturient montes, nascetur ridiculus mus. Nulla dui. Fusce feugiat malesuada odio. Morbi nunc odio, gravida at, cursus nec, luctus a, lorem.consec tetuer adipiscing elit. Praesent vestib ulum molest lacus aenean nonummy hendrerit mauris. Phasellus porta fusce suscipit varius mi. Cum sociis natoque penatibus et magnis.dis parturient montes, nascetur ridiculus mus. Nulla dui. Fusce feugiat malesuada odio. Morbi nunc odio, gravida at, cursus nec, luctus a, lorem.onsec tetuer adipiscing elit. Praesent vestib ulum molest lacus aenean nonummy hendrerit mauris. Phasellus porta fusce suscipit varius mi. Cum sociis natoque penatibus et magnis.dis parturient montes, nascetur ridiculus mus. Nulla dui. Fusce feugiat malesuada odio. Morbi nunc odio, gravida at, cursus nec, luctus a, lorem.</p>
    </div>
    <div class="links">
      <div>- <a href="#">Lorem ipsum dolorit amet tetuer</a></div><div>- <a href="#">Lorem ipsum dolorit amet tetuer</a></div>
      <div>- <a href="#">Adipiscing elit praesebutm molestie lacus</a></div><div>- <a href="#">Adipiscing elit praesebutm molestie lacus</a></div>
      <div>- <a href="#">Lorem ipsum dolorit amet tetuer</a></div><div>- <a href="#">Lorem ipsum dolorit amet tetuer</a></div>
      <div>- <a href="#">Adipiscing elit praesebutm molestie lacus</a></div><div>- <a href="#">Adipiscing elit praesebutm molestie lacus</a></div>
      <div>- <a href="#">Lorem ipsum dolorit amet tetuer</a></div><div>- <a href="#">Lorem ipsum dolorit amet tetuer</a></div>
      <div>- <a href="#">Adipiscing elit praesebutm molestie lacus</a></div><div>- <a href="#">Adipiscing elit praesebutm molestie lacus</a></div>
    </div>
    <span class="more" style="top:311px">[READ MORE]</span>
  </section>

  <footer class="footer">
    <span class="mark"></span>
    <span>BRIGHTCOILHEAT PTY LTD © 2011 &nbsp;|&nbsp; PRIVACY POLICY</span>
  </footer>
</div>
</body>
</html>
```